Brisket Dwelling Review is a leading provider of residential appraisal and home inspection products in S

I need a business card/logo designed that obviously describes my business. We are a residential appraisal and home inspection company in Springfield, MO. We offer residential appraisals, home inspection, pest inspection and radon gas measurement. We have been in business for 18 years and hold state certified residential appraisal licenses and VORMEL certified home inspection licenses. I have a logo that I really like and will attach, but would be open to new suggestions. I like more modern designs than traditional and would like a two sided card with our services, licenses and qualifications on the back.

```html
<!DOCTYPE html>
<html lang="en">
<head>
<meta charset="utf-8">
<title>Brisket Dwelling Review – Business Card</title>
<link href="https://fonts.googleapis.com/css2?family=Open+Sans:wght@400;600;700&display=swap" rel="stylesheet">
<style>
  :root {
    --page: #e9e4dc;
    --card-white: #ffffff;
    --card-black: #0c0c0c;
    --orange: #f0931e;
    --tan: #d9c3a0;
    --brown: #7a5c3a;
    --ink: #222222;
    --light: #f4f4f4;
  }
  * { margin: 0; padding: 0; box-sizing: border-box; }
  html, body { width: 1200px; height: 913px; overflow: hidden; }
  body {
    background: var(--page);
    font-family: "Open Sans", Arial, sans-serif;
    position: relative;
  }
  .card {
    position: absolute;
    width: 500px;
    height: 286px;
    border-radius: 14px;
    overflow: hidden;
    box-shadow: 0 8px 24px rgba(0,0,0,0.18);
  }
  .card-front { left: 60px; top: 313px; background: var(--card-white); }
  .card-back { left: 640px; top: 313px; background: var(--card-black); color: var(--light); }

  .front-swoosh { position: absolute; left: 0; top: 0; width: 500px; height: 286px; }

  .holder { position: absolute; left: 262px; right: 16px; top: 26px; border-left: 1px solid #cfcfcf; padding-left: 12px; }
  .holder-name { font-size: 19px; font-weight: 700; color: var(--ink); letter-spacing: 0.3px; white-space: nowrap; }
  .holder-role { font-size: 11px; color: var(--orange); font-weight: 600; margin-bottom: 8px; }
  .contact-list { list-style: none; font-size: 11px; color: var(--ink); }
  .contact-list li { display: flex; align-items: center; gap: 7px; height: 17px; white-space: nowrap; }
  .contact-list svg { width: 11px; height: 11px; fill: var(--orange); flex: none; }

  .brand-front { position: absolute; left: 30px; top: 164px; display: flex; align-items: center; gap: 12px; }
  .cert-badge { width: 34px; height: 34px; border-radius: 50%; background: #c9a63a; flex: none; }
  .brand-name { font-size: 21px; font-weight: 700; color: var(--brown); white-space: nowrap; }

  .address { position: absolute; left: 0; right: 0; bottom: 14px; text-align: center; font-size: 10.5px; color: var(--ink); }

  .brand-back { position: absolute; left: 0; right: 0; top: 40px; text-align: center; font-size: 24px; font-weight: 700; color: var(--tan); }
  .services { list-style: none; position: absolute; left: 0; right: 0; top: 90px; text-align: center; font-size: 13px; line-height: 18px; font-weight: 600; }
  .services .accent { color: var(--orange); }
  .tagline { position: absolute; left: 30px; right: 30px; bottom: 22px; text-align: center; font-size: 10px; line-height: 14px; color: var(--light); }
</style>
</head>
<body>
  <section class="card card-front">
    <svg class="front-swoosh" viewBox="0 0 500 286" aria-hidden="true">
      <path d="M0 286 L0 255 Q220 215 500 185 L500 286 Z" fill="var(--tan)"/>
      <path d="M0 255 Q220 215 500 185" fill="none" stroke="var(--orange)" stroke-width="5"/>
    </svg>
    <div class="holder">
      <p class="holder-name">MARLO TENNANT</p>
      <p class="holder-role">OWNER</p>
      <ul class="contact-list">
        <li><svg viewBox="0 0 24 24"><path d="M6.6 10.8a15 15 0 0 0 6.6 6.6l2.2-2.2a1 1 0 0 1 1-.25 11.4 11.4 0 0 0 3.6.57 1 1 0 0 1 1 1V20a1 1 0 0 1-1 1A17 17 0 0 1 3 4a1 1 0 0 1 1-1h3.5a1 1 0 0 1 1 1c0 1.25.2 2.45.57 3.57a1 1 0 0 1-.25 1z"/></svg>555-014-3414</li>
        <li><svg viewBox="0 0 24 24"><rect x="5" y="2" width="14" height="20" rx="2"/></svg>555-017-8936</li>
        <li><svg viewBox="0 0 24 24"><path d="M2 5h20v14H2z M2 5l10 8 10-8" stroke="#fff" stroke-width="1.5"/></svg>info@brisketdwellingreview.com</li>
        <li><svg viewBox="0 0 24 24"><circle cx="12" cy="12" r="10"/></svg>www.brisketdwellingreview.com</li>
      </ul>
    </div>
    <div class="brand-front">
      <span class="cert-badge" role="img" aria-label="Certification badge"></span>
      <span class="brand-name">Brisket Dwelling Review</span>
    </div>
    <p class="address">Brisket Dwelling Review 482 Larkspur Lane Suite B Fernvale, MO 65000</p>
  </section>

  <section class="card card-back">
    <p class="brand-back">Brisket Dwelling Review</p>
    <ul class="services">
      <li>APPRAISAL</li>
      <li class="accent">HOME INSPECTION</li>
      <li>TERMITE</li>
      <li class="accent">RADON</li>
      <li>WELL &amp; SEPTIC INSPECTION</li>
      <li class="accent">ENERGY AUDITS</li>
    </ul>
    <p class="tagline">With years of experience behind us, we're prepared to tackle anything from a first Time buyer's starter home or a seasoned buyer purchasing a luxurious dream home</p>
  </section>
</body>
</html>
```